SkyvoraQ Business Cards and Stationary Design

Need a design for our business cards and stationary. I want to carry on the theme of the logo. I want the business cards to have a design on the back. I would like the business cards and the stationary to carry the same theme, design scheme, and branding

Target Market(s)

Airlines and Maintenance Facilities

Industry/Entity Type

Aviation

Contact Information for Business Card

Name
Position Title
Address: 4827 Tollbeck Lane, Fort Pierce, Florida, 34951
Office Number
Mobile Number
Email
Website

Font styles to use
Serif
Sans Serif

Colors

Designer to choose colors to be used in the design.

```html
<!DOCTYPE html>
<html lang="en">
<head>
<meta charset="utf-8">
<title>SkyvoraQ Business Cards</title>
<link href="https://fonts.googleapis.com/css2?family=Barlow:wght@400;600&family=Tinos&display=swap" rel="stylesheet">
<style>
  :root {
    --backdrop: #e4e4e4;
    --card-grey: #dcdcdc;
    --card-border: #f6f6f6;
    --navy: #1d2c52;
    --brand-blue: #2a74c4;
    --ink: #1a1a1a;
  }
  html, body {
    margin: 0;
    padding: 0;
    width: 1200px;
    height: 1200px;
    overflow: hidden;
    background: var(--backdrop);
  }
  .canvas {
    position: relative;
    width: 1200px;
    height: 1200px;
  }
  .card {
    position: absolute;
    top: 450px;
    width: 507px;
    height: 290px;
    box-sizing: border-box;
  }
  .card-front {
    left: 42px;
    background: var(--card-grey);
    display: flex;
    flex-direction: column;
    align-items: center;
    justify-content: center;
    gap: 14px;
  }
  .brand-mark {
    width: 68px;
    height: 68px;
    border-radius: 50%;
    border: 5px solid var(--brand-blue);
    box-sizing: border-box;
  }
  .brand-name {
    font-family: "Barlow", sans-serif;
    font-weight: 600;
    font-size: 34px;
    letter-spacing: 5px;
    text-transform: uppercase;
    color: var(--navy);
    margin: 0;
  }
  .card-back {
    left: 650px;
    background: var(--card-border);
    padding: 23px 23px 21px 26px;
  }
  .back-panel {
    position: relative;
    width: 100%;
    height: 100%;
    background: var(--card-grey);
  }
  .corner-brand {
    position: absolute;
    top: 18px;
    right: 20px;
    display: flex;
    align-items: center;
    gap: 6px;
  }
  .corner-brand .brand-mark {
    width: 24px;
    height: 24px;
    border-width: 3px;
  }
  .corner-brand .brand-name {
    font-size: 13px;
    letter-spacing: 1.5px;
  }
  .contact {
    position: absolute;
    left: 26px;
    top: 62px;
    color: var(--ink);
  }
  .person-name {
    font-family: "Barlow", sans-serif;
    font-weight: 400;
    font-size: 25px;
    line-height: 1;
    margin: 0;
  }
  .person-name strong { font-weight: 600; }
  .person-role {
    font-family: "Tinos", serif;
    font-size: 15px;
    margin: 6px 0 0;
  }
  .divider {
    width: 65px;
    height: 2px;
    background: var(--ink);
    margin: 4px 0 6px;
  }
  .details {
    font-family: "Tinos", serif;
    font-size: 14px;
    line-height: 18px;
    margin: 0;
    list-style: none;
    padding: 0;
  }
  .details .gap { margin-top: 5px; }
</style>
</head>
<body>
<main class="canvas">
  <section class="card card-front">
    <span class="brand-mark"></span>
    <p class="brand-name">SkyvoraQ</p>
  </section>

  <section class="card card-back">
    <div class="back-panel">
      <div class="corner-brand">
        <span class="brand-mark"></span>
        <span class="brand-name">SkyvoraQ</span>
      </div>
      <div class="contact">
        <h1 class="person-name">Your <strong>Name</strong></h1>
        <p class="person-role">Manager</p>
        <div class="divider"></div>
        <ul class="details">
          <li>P: 555.318.4072</li>
          <li>P: 555.318.4072</li>
          <li class="gap">E: youremail@skyvoraq.com</li>
          <li class="gap">W: www.skyvoraq.com</li>
          <li class="gap">4827 Tollbeck Lane, Fort Pierce, Florida, 34951</li>
        </ul>
      </div>
    </div>
  </section>
</main>
</body>
</html>
```